Exciting, Bold and Modern Landscaping & Turf care company business card

Hello, I own a lawn and landscaping company in Virginia, USA. We would like to design a bold, dynamic, modern business card that really makes us stand out. I tire of all green business cards with crappy, cartoonish clipart grass on them. It needs to be two sided, on one side i need to highlight our turf care division called "Promised Brighter Meadow" We maintain grass, fertilize it, weed control, etc.. We have a green thumbed gopher as our logo that i will attach. I am looking for something, clean and neat but out of the box in style. Im open to all ideas, and would like different options for them. On the other side, i want to highlight our landscaping division "Quiet Harbor Landscaping" In this division we design and install landscapes. Feel free to visit our website for more info or email me with ANY questions. Our busines cards in the past have highlighted our different services, but i don't want to this time. By the time I hand out a business card we are usually already estimating a project and they know what services we offer. I do want them to look at my card and say "wow thats pretty cool" and for them to think "These guys are something different, not just your standard dirt diggers" The logo doesnt have to be on both sides, but it needs to be on the turf care side. Our phone number and website should also be on at least on side, but need not be on both. The phone number is (555)618-4072 as well as the web address as www.MossbrookYardWorks.example. I like for the web address to have caps like that becasue it makes the long address much easier to read. I would like it in full color, printing costs are not my major concern. I also love rounded corners or interesting die cut designs as well, so feel free to wow me. Whether it be a clean white background with a bold photo to an all black card with a gray logo except for his green thumb with silver foil lettering to anything in between, lets go for it. That bieng said i dont want anything cartoonish, we are still a professional service and i want that to come through. THANKS!
Updates
Project Deadline Extended
Reason: changed project to a committed payment. I would like designers to re-evaluate their interest now and give them extra time to submit designs. Thank you.
we have changed our status to a commited payment to entice more submissions. thank you all for your hard work!
Industry/Entity Type
Professional Service
Look and feel
Each slider illustrates characteristics of the customer's brand and the style your logo design should communicate.

```html
<!DOCTYPE html>
<html lang="en">
<head>
<meta charset="utf-8">
<title>Quiet Harbor Landscaping – Business Card</title>
<link href="https://fonts.googleapis.com/css2?family=Arimo:wght@700&family=Cinzel:wght@500&family=Open+Sans:wght@400&display=swap" rel="stylesheet">
<style>
  :root {
    --backdrop: #e9e6e1;
    --card: #000000;
    --turf-light: #c4e06a;
    --turf: #94bb2f;
    --turf-dark: #5d8a16;
    --silver-light: #d9d9d9;
    --silver: #a6a6a6;
    --silver-dark: #6e6e6e;
    --mascot-light: #cfcfcf;
    --mascot-dark: #5e5e5e;
    --contact: #ffffff;
  }
  * { margin: 0; padding: 0; box-sizing: border-box; }
  html, body {
    width: 1200px;
    height: 435px;
    overflow: hidden;
    background: var(--backdrop);
  }
  .canvas {
    position: relative;
    width: 1200px;
    height: 435px;
  }
  .card {
    position: absolute;
    width: 525px;
    height: 300px;
    background: var(--card);
  }
  .card--turf { left: 37px; top: 75px; }
  .card--landscape { left: 619px; top: 67px; }

  .mascot {
    position: absolute;
    left: 38px;
    top: 65px;
    width: 225px;
    height: 200px;
    border-radius: 40% 40% 10% 10%;
    background: radial-gradient(ellipse at 45% 40%, var(--mascot-light) 0%, var(--mascot-dark) 75%, #1a1a1a 100%);
  }

  .turf-slogan {
    position: absolute;
    left: 282px;
    top: 106px;
    width: 215px;
    text-align: center;
    font-family: "Arimo", Arial, sans-serif;
    font-weight: 700;
    line-height: 1;
    text-transform: uppercase;
    background: linear-gradient(180deg, var(--turf-light) 0%, var(--turf) 50%, var(--turf-dark) 100%);
    -webkit-background-clip: text;
    background-clip: text;
    color: transparent;
  }
  .turf-slogan span { display: block; }
  .turf-slogan__small { font-size: 23px; letter-spacing: 0.5px; margin-bottom: 6px; }
  .turf-slogan__mid { font-size: 33px; margin-bottom: 4px; }
  .turf-slogan__big { font-size: 37px; }

  .company-name {
    position: absolute;
    left: 0;
    top: 48px;
    width: 100%;
    text-align: center;
    font-family: "Cinzel", "Times New Roman", serif;
    font-weight: 500;
    font-size: 35px;
    line-height: 44px;
    letter-spacing: 1px;
    background: linear-gradient(180deg, var(--silver-light) 0%, var(--silver) 55%, var(--silver-dark) 100%);
    -webkit-background-clip: text;
    background-clip: text;
    color: transparent;
  }
  .company-name span { display: block; }

  .contact {
    position: absolute;
    left: 0;
    width: 100%;
    text-align: center;
    font-family: "Open Sans", Arial, sans-serif;
    color: var(--contact);
  }
  .contact--phone { top: 216px; font-size: 20px; letter-spacing: 1.5px; }
  .contact--web { top: 252px; font-size: 15px; letter-spacing: 1px; }
</style>
</head>
<body>
  <main class="canvas">
    <section class="card card--turf">
      <div class="mascot" role="img" aria-label="Grey gopher mascot with a green thumb giving a thumbs-up, standing in grass"></div>
      <h2 class="turf-slogan">
        <span class="turf-slogan__small">Promised</span>
        <span class="turf-slogan__mid">Brighter</span>
        <span class="turf-slogan__big">Meadow</span>
      </h2>
    </section>

    <section class="card card--landscape">
      <h1 class="company-name">
        <span>Quiet Harbor</span>
        <span>Landscaping</span>
      </h1>
      <p class="contact contact--phone">555-618-4072</p>
      <p class="contact contact--web">www.MOSSBROOKYARDWORKS.example</p>
    </section>
  </main>
</body>
</html>
```